Stationary pack for BrightVane

BrightVane is a recently establish Solar brokerage company based in Australia. We have a number of sales staff who provide advice and guidance to both residential and commercial customers regarding solar systems (solar hot water and solar panels.)

In addition to our brokerage services we are also developing software for the solar industry, which will be used to automate the solar system install process. This system will be used by other companies in the solar industry including installers, wholesalers and government departments.

We are after a stationary pack that consists of the following: Business cards, compliments slip and letter head.

The EPS, AI, PNG etc files for the logo are attached.

For the business card:
The name and logo of the company need to be clearly visible. On the back of the business cards, we would like the logo. I am happy for you to split the image part of the logo from the text if you think it would look better a different way.

I would like the business cards to be easily readable with the following information on the front:
Name
(Please leave room for titles for the future – eg Sales Advisor.)
Mobile
Office
Email
Address
ABN

Letter heads:
I would prefer the address to be at the top

Compliments slips:
Only need to be one sided

Target Market(s)

BrightVane provides services to both residential and commercial customers. Our customers will be environmentally conscious.

Industry/Entity Type

Residential

Requirements
Must have
• Business cards must have the logo on the back.

```html
<!DOCTYPE html>
<html lang="en">
<head>
<meta charset="utf-8">
<title>BrightVane Stationery Pack</title>
<link href="https://fonts.googleapis.com/css2?family=Questrial&display=swap" rel="stylesheet">
<style>
  :root {
    --sun: #f7a21b;
    --sun-light: #fcd24a;
    --sun-pale: #fde98a;
    --leaf: #5aa02c;
    --leaf-light: #a6cf3a;
    --mint: #dbead2;
    --mint-pale: #eef5ea;
    --paper: #ffffff;
    --ink-soft: #6aa83a;
    --edge: #7a7a7a;
  }
  * { box-sizing: border-box; margin: 0; padding: 0; }
  html, body { width: 1200px; height: 900px; overflow: hidden; background: var(--paper); }
  body { position: relative; font-family: "Questrial", sans-serif; }

  .brand { display: flex; align-items: center; gap: 6px; color: var(--leaf); font-family: "Questrial", sans-serif; font-weight: 400; white-space: nowrap; }
  .brand-dot { border-radius: 50%; background: var(--leaf-light); flex: none; }

  /* Letterhead */
  .letterhead { position: absolute; left: 76px; top: 44px; width: 638px; height: 826px; background: var(--paper); overflow: hidden; }
  .letterhead-band { position: absolute; left: 0; top: 0; }
  .letterhead .brand { position: absolute; left: 16px; top: 66px; width: 124px; font-size: 19px; gap: 5px; }
  .letterhead .brand-dot { width: 13px; height: 13px; }
  .letterhead-divider { position: absolute; left: 148px; top: 28px; width: 2px; height: 110px; background: var(--leaf-light); }
  .letterhead-contact { position: absolute; left: 158px; top: 30px; color: var(--ink-soft); }
  .contact-name { font-size: 15px; }
  .contact-title { font-size: 10px; margin-top: 4px; }
  .contact-lines { font-size: 7px; line-height: 10px; margin-top: 12px; list-style: none; }
  .letterhead-footer { position: absolute; left: 0; bottom: 0; }

  .fold-line { position: absolute; left: 713px; top: 44px; width: 2px; height: 386px; background: var(--sun); }

  /* Business cards */
  .card-back { position: absolute; left: 752px; top: 48px; width: 262px; height: 150px; background: radial-gradient(ellipse at center, var(--sun-pale) 0%, var(--sun-light) 40%, var(--sun) 100%); border: 1px solid #c98a1a; display: flex; align-items: center; justify-content: center; }
  .card-back .brand { font-size: 24px; }
  .card-back .brand-dot { width: 18px; height: 18px; }

  .card-front { position: absolute; left: 752px; top: 232px; width: 262px; height: 152px; background: var(--paper); border: 1px solid var(--edge); overflow: hidden; }
  .card-front-art { position: absolute; right: 0; bottom: 0; }
  .card-front-contact { position: absolute; left: 8px; top: 8px; color: var(--ink-soft); }
  .card-front-contact .contact-name { font-size: 13px; }
  .card-front-contact .contact-title { font-size: 10px; margin-top: 2px; }
  .card-front-contact .contact-lines { font-size: 8px; line-height: 10px; margin-top: 10px; }
  .card-front .brand { position: absolute; left: 8px; bottom: 8px; font-size: 12px; gap: 4px; }
  .card-front .brand-dot { width: 9px; height: 9px; }

  /* Compliments slip */
  .comp-slip { position: absolute; left: 654px; top: 426px; width: 504px; height: 216px; border: 16px solid var(--sun); background: var(--paper); overflow: hidden; }
  .comp-slip-art { position: absolute; right: 0; bottom: 0; }
  .comp-slip .brand { position: absolute; left: 10px; top: 20px; font-size: 17px; gap: 5px; }
  .comp-slip .brand-dot { width: 14px; height: 14px; }
</style>
</head>
<body>

<section class="letterhead" aria-label="Letterhead">
  <svg class="letterhead-band" width="638" height="260" viewBox="0 0 638 260">
    <defs>
      <linearGradient id="bandSun" x1="0" y1="0" x2="1" y2="0">
        <stop offset="0" stop-color="#f7a21b"/>
        <stop offset="1" stop-color="#fbb52a"/>
      </linearGradient>
      <linearGradient id="bandLeaf" x1="1" y1="0" x2="0" y2="0">
        <stop offset="0" stop-color="#4f9a2c"/>
        <stop offset="0.6" stop-color="#a6cf3a"/>
        <stop offset="1" stop-color="#d9e98a"/>
      </linearGradient>
    </defs>
    <path d="M0 0 H638 V54 C470 80 250 150 0 210 Z" fill="url(#bandSun)"/>
    <path d="M638 54 C470 80 250 150 0 210 V206 C230 170 420 110 638 90 Z" fill="url(#bandLeaf)"/>
    <path d="M0 210 C250 150 470 80 638 54 V66 C460 100 260 170 0 210 Z" fill="#e4c23a"/>
  </svg>
  <div class="brand"><span class="brand-dot"></span>BrightVane</div>
  <div class="letterhead-divider"></div>
  <div class="letterhead-contact">
    <p class="contact-name">Name</p>
    <p class="contact-title">Sales Advisor</p>
    <ul class="contact-lines">
      <li>Mobile</li><li>Office</li><li>Email</li><li>Address</li><li>ABN</li>
    </ul>
  </div>
  <svg class="letterhead-footer" width="638" height="340" viewBox="0 0 638 340">
    <defs>
      <linearGradient id="panelGlow" x1="0" y1="1" x2="1" y2="0">
        <stop offset="0" stop-color="#fde98a"/>
        <stop offset="0.5" stop-color="#eef5ea"/>
        <stop offset="1" stop-color="#dbead2"/>
      </linearGradient>
    </defs>
    <path d="M0 340 C120 170 380 60 638 40 V340 Z" fill="url(#panelGlow)" role="img" aria-label="Soft solar panel field"/>
    <path d="M0 300 C140 150 380 40 638 22 V40 C380 60 130 180 10 340 H0 Z" fill="#f7a21b"/>
    <path d="M140 340 C260 240 450 180 638 170 V190 C460 200 280 260 180 340 Z" fill="#f9b52e"/>
  </svg>
</section>

<div class="fold-line"></div>

<section class="card-back" aria-label="Business card back">
  <div class="brand"><span class="brand-dot"></span>BrightVane</div>
</section>

<section class="card-front" aria-label="Business card front">
  <svg class="card-front-art" width="180" height="110" viewBox="0 0 180 110" role="img" aria-label="Soft solar panel field">
    <defs>
      <linearGradient id="cardPanel" x1="0" y1="1" x2="1" y2="0">
        <stop offset="0" stop-color="#ffffff"/>
        <stop offset="1" stop-color="#dbead2"/>
      </linearGradient>
    </defs>
    <path d="M0 110 C50 50 120 15 180 5 V110 Z" fill="url(#cardPanel)"/>
  </svg>
  <div class="card-front-contact">
    <p class="contact-name">Name</p>
    <p class="contact-title">Sales Advisor</p>
    <ul class="contact-lines">
      <li>Mobile</li><li>Office</li><li>Email</li><li>Address</li><li>ABN</li>
    </ul>
  </div>
  <div class="brand"><span class="brand-dot"></span>BrightVane</div>
</section>

<section class="comp-slip" aria-label="Compliments slip">
  <svg class="comp-slip-art" width="340" height="184" viewBox="0 0 340 184" role="img" aria-label="Soft solar panel field">
    <defs>
      <linearGradient id="slipPanel" x1="0" y1="1" x2="1" y2="0">
        <stop offset="0" stop-color="#ffffff"/>
        <stop offset="0.5" stop-color="#eef5ea"/>
        <stop offset="1" stop-color="#dbead2"/>
      </linearGradient>
    </defs>
    <path d="M0 184 C80 90 200 25 340 0 V184 Z" fill="url(#slipPanel)"/>
  </svg>
  <div class="brand"><span class="brand-dot"></span>BrightVane</div>
</section>

</body>
</html>
```